New Business Card Design Project

I have a logo I would like to use on the business card. I want something that will stand out and that will be remembered.

Target Market(s)

People who collect gems, minerals and crystals.

Contact Information for Business Card

email - tkstonefalcon@mailbrook.net
phone # 617-203-4958

Font styles to use
Serif
Sans Serif
Decorative

Colors

Designer to choose colors to be used in the design.

Requirements
Must have
• The logo...two to choose from.
Nice to have
• An eye catching and memorable way to draw in people who collect gems minerals and crystals.

```html
<!DOCTYPE html>
<html lang="en">
<head>
<meta charset="utf-8">
<title>Stone Falcon – Business Card</title>
<link rel="stylesheet" href="https://fonts.googleapis.com/css2?family=Oswald:wght@700&family=Work+Sans:wght@400;500&display=swap">
<style>
  :root {
    --page: #141414;
    --card: #1d1d1d;
    --card-edge: #262626;
    --foil: #cfcfcf;
    --foil-soft: #9a9a9a;
    --emboss: #2c2c2c;
    --rule: #5a5a5a;
  }
  * { margin: 0; padding: 0; box-sizing: border-box; }
  html, body {
    width: 1200px; height: 900px; overflow: hidden;
    background: var(--page);
  }
  .canvas {
    position: relative; width: 1200px; height: 900px;
    background: radial-gradient(ellipse at 50% 40%, #1c1c1c 0%, var(--page) 70%);
  }
  .card {
    position: absolute; left: 280px; width: 640px; height: 366px;
    background: var(--card);
    border: 1px solid var(--card-edge);
    box-shadow: 0 14px 30px rgba(0,0,0,.55);
  }
  .card--front { top: 60px; }
  .card--back { top: 474px; }

  .brand {
    position: absolute; display: flex; flex-direction: column; align-items: center;
  }
  .card--front .brand { left: 0; right: 0; top: 62px; }
  .brand__art {
    width: 150px; height: 130px; border-radius: 50% 50% 14px 14px;
  }
  .card--front .brand__art { background: linear-gradient(160deg, #d8d8d8, #7c7c7c); }
  .brand__name {
    margin-top: 14px;
    font-family: "Oswald", sans-serif; font-weight: 700;
    font-size: 46px; letter-spacing: 1px; text-transform: uppercase;
    color: var(--foil); line-height: 1;
  }
  .card--back .brand { left: 40px; top: 82px; width: 230px; }
  .card--back .brand__art { width: 120px; height: 104px; background: var(--emboss); }
  .card--back .brand__name { font-size: 36px; color: var(--emboss); }

  .divider {
    position: absolute; left: 300px; top: 60px; width: 1px; height: 240px;
    background: var(--rule);
  }
  .contact {
    position: absolute; left: 340px; top: 78px;
    font-family: "Work Sans", sans-serif; color: var(--foil);
  }
  .contact__name { font-size: 26px; font-weight: 500; letter-spacing: 2px; text-transform: uppercase; }
  .contact__role { font-size: 16px; color: var(--foil-soft); margin-top: 2px; }
  .contact__address { font-size: 17px; line-height: 1.45; margin-top: 18px; letter-spacing: .5px; }
  .contact__list { list-style: none; margin-top: 12px; font-size: 17px; line-height: 1.5; letter-spacing: .5px; }
  .contact__list li { display: flex; align-items: center; gap: 10px; }
  .contact__list svg { width: 12px; height: 12px; flex: none; }
</style>
</head>
<body>
<main class="canvas">
  <section class="card card--front">
    <div class="brand">
      <div class="brand__art" role="img" aria-label="Brand mascot illustration in silver foil"></div>
      <div class="brand__name">Stone Falcon</div>
    </div>
  </section>

  <section class="card card--back">
    <div class="brand">
      <div class="brand__art" role="img" aria-label="Blind-embossed brand mascot illustration"></div>
      <div class="brand__name">Stone Falcon</div>
    </div>
    <div class="divider"></div>
    <div class="contact">
      <div class="contact__name">Daniel Hart</div>
      <div class="contact__role">Director</div>
      <p class="contact__address">58 Harbour Lane,<br>Nelson, NZ, 7010</p>
      <ul class="contact__list">
        <li>
          <svg viewBox="0 0 12 12" aria-hidden="true"><path d="M3 1 L5 3.5 L4 4.8 Q5 7 7.2 8 L8.5 7 L11 9 L9.8 11 Q5 11 2.5 7.5 Q1 5 1.2 2.3 Z" fill="var(--foil)"/></svg>
          617-203-4958
        </li>
        <li>
          <svg viewBox="0 0 12 12" aria-hidden="true"><rect x="1" y="2.5" width="10" height="7" fill="none" stroke="var(--foil)" stroke-width="1.2"/><path d="M1 3 L6 7 L11 3" fill="none" stroke="var(--foil)" stroke-width="1.2"/></svg>
          tkstonefalcon@mailbrook.net
        </li>
        <li>
          <svg viewBox="0 0 12 12" aria-hidden="true"><circle cx="6" cy="6" r="5" fill="none" stroke="var(--foil)" stroke-width="1.1"/><ellipse cx="6" cy="6" rx="2.2" ry="5" fill="none" stroke="var(--foil)" stroke-width="1"/><path d="M1 6 H11" stroke="var(--foil)" stroke-width="1"/></svg>
          www.tkstonefalcon.com
        </li>
      </ul>
    </div>
  </section>
</main>
</body>
</html>
```